Wine labels Velmora Wine Council - Nueva etiqueta El Consejo Regulador de vinos de Albarrán

Velmora Wines Council, based in southern Spain, are looking to create a new suite of wine labels which retain the elegance of the Velmora Wines industry while reinvigorating their image to the modern era and a new generation of Sherry Wine lovers. These labels will be used across the Velmora Wines Council's range of wines for the promotion of the Velmora Wines industry.

Your design must present at least two styles of Velmora Wines which demonstrate an elegant, modern interpretation and understanding of the unique mood and personality for these wines and the essence of southern Spain.

10 labels will be created based on the winning design, one for each of the unique varieties of Velmora Wines within the collection. This collection comprises of several different wine varieties including: Fino, Manzanilla, Amontillado, Oloroso, Palo Cortado, Medium, Cream, Pale Cream, Pedro Ximenez and Moscatel.

We recommend you visit our website www.velmora-vinos.example/wines as the source to understanding the origins and unique personality of these diverse wines.

El Consejo Regulador de los Vinos de Albarrán y Tordesal quiere renovar las etiquetas de los vinos utilizados para sus actividades de promoción genérica. Esta colección de vinos comprende las tipologías más importantes de la región que incluye: fino, manzanilla, amontillado, oloroso, palo cortado, pale cream, medium, cream, pedro ximénez y moscatel. Por lo tanto se precisan 10 etiquetas, una para cada uno de los vinos mencionados.
Updates

Project Deadline Extended
Reason: Due to some confusion with the deadline we wish to officially extend the deadline to allow designers one last week to submit their entries.

Target Market(s)

Industry, journalists, media, sommeliers, chefs, wine writers

Industry/Entity Type

Council

Requirements
Must have
• Front and Back label plus capsule:
• Front label can have either of the two official logos of the Velmora Wine council titled Vinos de Albarrán Digital or not, this is optional. Must include: Vino selecionado por el Consejo Regulador de la Denominacion de Origen, Name of the variety of wine eg FINO, percentage of alcohol eg 15% and quantity 75 cl.
• The back of the label must include the council logo titled Sellora and 4 additional logos positioned smaller. The Europa logo must appear larger than the 3 other logos. Space for descriptive text about the wine is also required.
• The dimensions of the bottle can be found at this link http://www.vidrialto.example/es/catalogo/vinos-y-espumosos/bordelesas/bd-orla
• Altura:305 mm
• Diámetro base:76,20 mm
• Diámetro hombro:82 mm
• Tipo boca:Cetie
• Peso:750 gr
• Capacidad:75 cl
• Etiqueta delantera y trasera y capsula
• La etiqueta delantera puede incluir el logo oficial del Consejo Regulador o el logo digital, o ninguno, esto es opcional. Debe incluir el siguiete texto: Vino selecionado por el Consejo Regulador de la Denominacion de Origen, el nombre de la variedad del vino, por ejemplo Fino, el porcentaje de alcohol, por ejemplo 15%, y la capacidad 75cl.
• La etiqueta trasera debe incluir el logo oficial Sellora del Consejo, y cuatro logos adicionales con una dimension menor. El Logo de ¨Europa invierte en las zonas rurales¨ debe ser de mayor tamaño que los otros. Se precisa espacio para el texto descriptivo de los vinos.
• Las dimensiones de la botella se puede encontrar en este enlace
• http://www.vidrialto.example/es/catalogo/vinos-y-espumosos/bordelesas/bd-orla
• Altura:305 mm
• Diámetro base:76,20 mm
• Diámetro hombro:82 mm
• Tipo boca:Cetie
• Peso:750 gr
• Capacidad:75 cl
Nice to have
• See our website velmora-vinos.example to understand the origin of the wines. Ver nuestra página web velmora-vinos.example para mejor entender los vinos.
Should not have
• Images of catavinos or stereotypical images from Spain such as flamenco dancers or guitars.

```html
<!DOCTYPE html>
<html lang="es">
<head>
<meta charset="utf-8">
<title>Vinos de Albarrán — Etiquetas</title>
<link rel="stylesheet" href="https://fonts.googleapis.com/css2?family=Cinzel:wght@400;500&family=EB+Garamond:wght@400;500&display=swap">
<style>
  :root {
    --canvas: #ececec;
    --ink: #141414;
    --gold: #c9a24a;
    --gold-light: #e2c57a;
    --paper-text: #2a2a2a;
    --muted-dark: #6b6b6b;
    --muted-light: #a9a9a9;
    --manzanilla: #d9d9db;
    --fino: #d8d5bd;
    --pale-cream: #a9c3c2;
    --medium: #d6bfb6;
    --amontillado: #c4d6c3;
  }
  * { margin: 0; padding: 0; box-sizing: border-box; }
  html, body { width: 1200px; height: 1200px; overflow: hidden; }
  body {
    background: var(--canvas);
    display: flex;
    align-items: center;
    justify-content: center;
  }
  .label-range {
    display: flex;
    gap: 26px;
  }
  .label {
    position: relative;
    width: 206px;
    height: 262px;
    overflow: hidden;
    box-shadow: 0 2px 8px rgba(0,0,0,0.12);
  }
  .label__art {
    position: absolute;
    inset: 0;
    width: 100%;
    height: 100%;
  }
  .label__brand {
    position: absolute;
    top: 50px;
    left: 0; right: 0;
    text-align: center;
    font-family: "Cinzel", serif;
    font-weight: 500;
    color: var(--gold);
    line-height: 1.15;
  }
  .label__brand-name { display: block; font-size: 11px; letter-spacing: 0.2px; }
  .label__brand-sub { display: block; font-size: 5.5px; letter-spacing: 1.6px; }
  .label__variety {
    position: absolute;
    top: 180px;
    left: 0; right: 0;
    text-align: center;
    font-family: "Cinzel", serif;
    font-size: 17px;
    letter-spacing: 0.5px;
  }
  .label__origin {
    position: absolute;
    top: 220px;
    left: 30px; right: 30px;
    text-align: center;
    font-family: "EB Garamond", serif;
    font-size: 5.6px;
    line-height: 1.35;
  }
  .label__volume {
    position: absolute;
    top: 242px;
    left: 0; right: 0;
    text-align: center;
    font-family: "EB Garamond", serif;
    font-weight: 500;
    font-size: 7.5px;
    letter-spacing: 0.3px;
  }
  .label__volume .divider { padding: 0 3px; }

  .label--dark-top .label__variety,
  .label--dark-top .label__volume { color: var(--paper-text); }
  .label--dark-top .label__origin { color: var(--muted-dark); }
  .label--light-top .label__variety,
  .label--light-top .label__volume { color: #f2f2f2; }
  .label--light-top .label__origin { color: var(--muted-light); }
</style>
</head>
<body>
  <main class="label-range">

    <article class="label label--dark-top">
      <svg class="label__art" viewBox="0 0 206 262" preserveAspectRatio="none" aria-hidden="true">
        <rect width="206" height="262" fill="var(--manzanilla)"/>
        <path d="M0 0H206V108Q103 156 0 108Z" fill="var(--ink)"/>
        <path d="M0 108Q103 156 206 108" fill="none" stroke="var(--gold)" stroke-width="1.6"/>
        <circle cx="103" cy="120" r="23" fill="var(--ink)" stroke="var(--gold-light)" stroke-width="1.5"/>
      </svg>
      <p class="label__brand"><span class="label__brand-name">Vinos de Albarrán</span><span class="label__brand-sub">Velmora Wines</span></p>
      <h2 class="label__variety">Manzanilla</h2>
      <p class="label__origin">Vino seleccionado por el Consejo Regulador de la Denominacion de Origen</p>
      <p class="label__volume">15% ALC/VOL<span class="divider">|</span>75 CL</p>
    </article>

    <article class="label label--light-top">
      <svg class="label__art" viewBox="0 0 206 262" preserveAspectRatio="none" aria-hidden="true">
        <rect width="206" height="262" fill="var(--ink)"/>
        <path d="M0 0H206V108Q103 156 0 108Z" fill="var(--fino)"/>
        <path d="M0 108Q103 156 206 108" fill="none" stroke="var(--gold)" stroke-width="1.6"/>
        <circle cx="103" cy="120" r="23" fill="var(--ink)" stroke="var(--gold-light)" stroke-width="1.5"/>
      </svg>
      <p class="label__brand"><span class="label__brand-name">Vinos de Albarrán</span><span class="label__brand-sub">Velmora Wines</span></p>
      <h2 class="label__variety">Fino</h2>
      <p class="label__origin">Vino seleccionado por el Consejo Regulador de la Denominacion de Origen</p>
      <p class="label__volume">15% ALC/VOL<span class="divider">|</span>75 CL</p>
    </article>

    <article class="label label--dark-top">
      <svg class="label__art" viewBox="0 0 206 262" preserveAspectRatio="none" aria-hidden="true">
        <rect width="206" height="262" fill="var(--pale-cream)"/>
        <path d="M0 0H206V108Q103 156 0 108Z" fill="var(--ink)"/>
        <path d="M0 108Q103 156 206 108" fill="none" stroke="var(--gold)" stroke-width="1.6"/>
        <circle cx="103" cy="120" r="23" fill="var(--ink)" stroke="var(--gold-light)" stroke-width="1.5"/>
      </svg>
      <p class="label__brand"><span class="label__brand-name">Vinos de Albarrán</span><span class="label__brand-sub">Velmora Wines</span></p>
      <h2 class="label__variety">Pale Cream</h2>
      <p class="label__origin">Vino seleccionado por el Consejo Regulador de la Denominacion de Origen</p>
      <p class="label__volume">15% ALC/VOL<span class="divider">|</span>75 CL</p>
    </article>

    <article class="label label--light-top">
      <svg class="label__art" viewBox="0 0 206 262" preserveAspectRatio="none" aria-hidden="true">
        <rect width="206" height="262" fill="var(--ink)"/>
        <path d="M0 0H206V108Q103 156 0 108Z" fill="var(--medium)"/>
        <path d="M0 108Q103 156 206 108" fill="none" stroke="var(--gold)" stroke-width="1.6"/>
        <circle cx="103" cy="120" r="23" fill="var(--ink)" stroke="var(--gold-light)" stroke-width="1.5"/>
      </svg>
      <p class="label__brand"><span class="label__brand-name">Vinos de Albarrán</span><span class="label__brand-sub">Velmora Wines</span></p>
      <h2 class="label__variety">Medium</h2>
      <p class="label__origin">Vino seleccionado por el Consejo Regulador de la Denominacion de Origen</p>
      <p class="label__volume">15% ALC/VOL<span class="divider">|</span>75 CL</p>
    </article>

    <article class="label label--dark-top">
      <svg class="label__art" viewBox="0 0 206 262" preserveAspectRatio="none" aria-hidden="true">
        <rect width="206" height="262" fill="var(--amontillado)"/>
        <path d="M0 0H206V108Q103 156 0 108Z" fill="var(--ink)"/>
        <path d="M0 108Q103 156 206 108" fill="none" stroke="var(--gold)" stroke-width="1.6"/>
        <circle cx="103" cy="120" r="23" fill="var(--ink)" stroke="var(--gold-light)" stroke-width="1.5"/>
      </svg>
      <p class="label__brand"><span class="label__brand-name">Vinos de Albarrán</span><span class="label__brand-sub">Velmora Wines</span></p>
      <h2 class="label__variety">Amontillado</h2>
      <p class="label__origin">Vino seleccionado por el Consejo Regulador de la Denominacion de Origen</p>
      <p class="label__volume">15% ALC/VOL<span class="divider">|</span>75 CL</p>
    </article>

  </main>
</body>
</html>
```